Stationery Design Project

I need a design that is simple, clean and modern, in square style, bold font.
The majority of the design needs to be White and Black with a splash of Red colour.
I would like a design for business cards and letter heads with the following information.
Name, Title, Phone, Fax, Email, Website and company ABN number

Target Market(s)

25 to 65 years old real estate clients

Industry/Entity Type

Business

Requirements
Must have
• All designs must incorporate Company Logo, Name, Title, Phone, Fax, Email, Website and company ABN number

```html
<!DOCTYPE html>
<html lang="en">
<head>
<meta charset="utf-8">
<title>Kestrel Real Estate — Business Card</title>
<link rel="stylesheet" href="https://fonts.googleapis.com/css2?family=PT+Sans:wght@400;700&display=swap">
<style>
  :root {
    --backdrop: #8f5c3b;
    --paper: #ffffff;
    --brand-red: #bd1e2d;
    --ink: #1c1c1c;
    --ink-soft: #4a4a4a;
    --on-red: #ffffff;
  }
  * { box-sizing: border-box; margin: 0; padding: 0; }
  html, body { width: 1200px; height: 402px; overflow: hidden; }
  body {
    background: var(--backdrop);
    font-family: "PT Sans", Arial, sans-serif;
    position: relative;
  }
  .card {
    position: absolute;
    top: 56px;
    width: 512px;
    height: 292px;
    overflow: hidden;
  }
  .card--front { left: 58px; background: var(--paper); }
  .card--back { left: 634px; background: var(--brand-red); }

  .card__wave { position: absolute; inset: 0; width: 512px; height: 292px; }

  .brand-frame {
    position: absolute;
    display: flex;
    flex-direction: column;
    align-items: center;
    justify-content: center;
    font-weight: 700;
    text-align: center;
  }
  .card--front .brand-frame {
    left: 38px; top: 40px; width: 232px; height: 130px;
    border: 3px solid var(--ink);
    border-radius: 14px;
    color: var(--ink);
  }
  .card--back .brand-frame {
    left: 103px; top: 42px; width: 308px; height: 170px;
    border: 4px solid var(--on-red);
    border-radius: 22px;
    color: var(--on-red);
  }
  .brand-frame__name { letter-spacing: 2px; line-height: 1; }
  .brand-frame__tag { letter-spacing: 8px; margin-top: 10px; }
  .card--front .brand-frame__name { font-size: 40px; }
  .card--front .brand-frame__tag { font-size: 11px; }
  .card--back .brand-frame__name { font-size: 54px; }
  .card--back .brand-frame__tag { font-size: 14px; letter-spacing: 11px; margin-top: 14px; }

  .person {
    position: absolute; right: 12px; top: 40px; text-align: right;
  }
  .person__name { color: var(--brand-red); font-weight: 700; font-size: 16px; line-height: 1.1; }
  .person__title { color: var(--ink-soft); font-size: 14px; line-height: 1.25; }

  .address {
    position: absolute; left: 42px; top: 207px;
    color: var(--ink-soft); font-size: 14px; line-height: 19px;
  }

  .contact {
    position: absolute; right: 14px; top: 220px;
    list-style: none; color: var(--on-red); font-size: 13px; line-height: 16.5px;
  }
  .contact li { display: flex; align-items: center; justify-content: flex-end; gap: 5px; }
  .contact svg { width: 10px; height: 10px; fill: var(--on-red); }

  .abn {
    position: absolute; left: 0; width: 512px; top: 228px;
    text-align: center; color: var(--on-red); font-size: 17px;
  }
</style>
</head>
<body>
  <section class="card card--front">
    <svg class="card__wave" viewBox="0 0 512 292" aria-hidden="true">
      <path d="M0,278 C150,268 360,230 512,158 L512,292 L0,292 Z" fill="var(--brand-red)"/>
      <path d="M0,246 C50,276 190,274 330,232 C200,262 70,272 0,258 Z" fill="var(--ink)"/>
    </svg>

    <div class="brand-frame">
      <span class="brand-frame__name">KESTREL</span>
      <span class="brand-frame__tag">REAL ESTATE</span>
    </div>

    <div class="person">
      <p class="person__name">Your Name</p>
      <p class="person__title">Title</p>
    </div>

    <address class="address" style="font-style:normal">
      Street Name, City Name<br>State, City Zip Code
    </address>

    <ul class="contact">
      <li><svg viewBox="0 0 10 10"><circle cx="5" cy="5" r="4.3" fill="none" stroke="#fff" stroke-width="1"/><path d="M3.3 2.6l1 1-.5.7c.4.8.9 1.3 1.7 1.7l.7-.5 1 1-.6.8C4.7 7 3 5.3 2.6 3.2z"/></svg>123-456-7890</li>
      <li><svg viewBox="0 0 10 10"><path d="M2 2h6l1 3v3H1V5zM2.6 3L2.1 4.6h5.8L7.4 3z"/><rect x="0.5" y="8" width="2" height="1.6"/><rect x="7.5" y="8" width="2" height="1.6"/></svg>123-456-7890</li>
      <li><svg viewBox="0 0 10 10"><path d="M1 2.5h8v5H1z M1.4 3l3.6 2.6L8.6 3"/></svg>info@kestrelrealty.com</li>
      <li><svg viewBox="0 0 10 10"><circle cx="5" cy="5" r="4.5"/><path d="M0.8 5h8.4M5 0.5v9" stroke="var(--brand-red)" stroke-width="0.8"/></svg>www.website.com</li>
    </ul>
  </section>

  <section class="card card--back">
    <div class="brand-frame">
      <span class="brand-frame__name">KESTREL</span>
      <span class="brand-frame__tag">REAL ESTATE</span>
    </div>
    <p class="abn">ABN;123456789</p>
  </section>
</body>
</html>
```